Creative Agency Showcase/Profile

Looking for a impactful, clean design to showcase our best works.

Our events company: www.brightkiteevents.com.sg

We have a clean and impactful look which we want to maintain. Looking at how we can best showcase our works/events to new customers who we want to do business with.

Actual photos will be provided once appointed.

Target Market(s)

Corporates, New Customers

Font styles to use
Sans Serif

Colors
ec1f27
0592cd
f78f20
6b439b
ffffff

Requirements
Must have
• Key Tagline:
• BREAKING NEW GROUND
• To be presented on a 16:9 Landscape format (prefably editable in KEYNOTE in the future)
• Total should be at least 8-10 pages including a COVER PAGE and CONTACT US PAGE.
Nice to have
• Some secondary captions/by lines.
• Must include event pictures.
• Hoping to have one picture per slide.
• Please use stock images at least 8-10 for now.

```html
<!DOCTYPE html>
<html lang="en">
<head>
<meta charset="utf-8">
<title>Event Showcase Slides</title>
<link rel="stylesheet" href="https://fonts.googleapis.com/css2?family=Montserrat:wght@500;900&display=swap">
<style>
  :root {
    --stage: #1c1c1c;
    --paper: #ffffff;
    --blush-panel: rgba(250, 105, 110, 0.86);
    --signal-red: rgba(226, 44, 42, 0.95);
    --frame-line: #ffffff;
  }
  * { margin: 0; padding: 0; box-sizing: border-box; }
  html, body {
    width: 1200px;
    height: 720px;
    overflow: hidden;
    background: linear-gradient(135deg, #6a6a6a 0%, #3a3a3a 38%, #101010 38.1%, #0c0c0c 100%);
    font-family: "Montserrat", Arial, sans-serif;
  }
  .slide {
    position: absolute;
    top: 202px;
    width: 564px;
    height: 317px;
    overflow: hidden;
    background: var(--paper);
    box-shadow: 0 6px 14px rgba(0, 0, 0, 0.45);
  }
  .slide--celebration { left: 26px; }
  .slide--nightshow { left: 608px; }
  .slide__art {
    position: absolute;
    inset: 0;
    width: 564px;
    height: 317px;
  }
  .title-panel {
    position: absolute;
    left: 22px;
    top: 22px;
    width: 156px;
    height: 190px;
    background: var(--blush-panel);
  }
  .slide__title {
    position: absolute;
    left: 58px;
    top: 38px;
    color: var(--paper);
    font-weight: 900;
    font-size: 33px;
    line-height: 29px;
    letter-spacing: -1.4px;
  }
  .slide__lede {
    position: absolute;
    left: 39px;
    top: 160px;
    width: 124px;
    color: var(--paper);
    font-weight: 500;
    font-size: 5.2px;
    line-height: 6px;
    text-align: justify;
  }
  .info-panel {
    position: absolute;
    left: 506px;
    top: 22px;
    width: 156px;
    height: 190px;
    margin-left: -120px;
    background: var(--signal-red);
    padding: 30px 16px 0 18px;
    box-shadow: 0 3px 8px rgba(0, 0, 0, 0.3);
  }
  .info-panel p {
    color: var(--paper);
    font-weight: 500;
    font-size: 5.2px;
    line-height: 6px;
    text-align: justify;
    margin-bottom: 8px;
  }
</style>
</head>
<body>

<section class="slide slide--celebration">
  <svg class="slide__art" viewBox="0 0 705 396" preserveAspectRatio="none">
    <defs>
      <clipPath id="celebrationShape">
        <polygon points="352,0 705,0 705,238 578,396 0,396 0,308"/>
      </clipPath>
      <linearGradient id="celebrationBase" x1="0" y1="0" x2="0.4" y2="1">
        <stop offset="0" stop-color="#f7a7bd"/>
        <stop offset="0.5" stop-color="#f28cb0"/>
        <stop offset="1" stop-color="#cf3f93"/>
      </linearGradient>
      <radialGradient id="celebrationHaze" cx="0.5" cy="0.5" r="0.5">
        <stop offset="0" stop-color="#ffe6ec" stop-opacity="0.95"/>
        <stop offset="1" stop-color="#ffe6ec" stop-opacity="0"/>
      </radialGradient>
      <radialGradient id="celebrationBlush" cx="0.5" cy="0.5" r="0.5">
        <stop offset="0" stop-color="#fbd0da" stop-opacity="0.9"/>
        <stop offset="1" stop-color="#fbd0da" stop-opacity="0"/>
      </radialGradient>
      <radialGradient id="celebrationMagenta" cx="0.5" cy="0.5" r="0.5">
        <stop offset="0" stop-color="#c2278c" stop-opacity="0.85"/>
        <stop offset="1" stop-color="#c2278c" stop-opacity="0"/>
      </radialGradient>
    </defs>
    <g role="img" aria-label="Photo of champagne glasses and a ribboned rosé bottle in soft pink light" clip-path="url(#celebrationShape)">
      <rect width="705" height="396" fill="url(#celebrationBase)"/>
      <ellipse cx="470" cy="90" rx="280" ry="120" fill="url(#celebrationHaze)"/>
      <ellipse cx="430" cy="230" rx="200" ry="110" fill="url(#celebrationBlush)"/>
      <ellipse cx="570" cy="230" rx="70" ry="170" fill="url(#celebrationBlush)"/>
      <ellipse cx="150" cy="380" rx="260" ry="110" fill="url(#celebrationMagenta)"/>
    </g>
    <polyline points="270,88 353,30 676,30 676,228 590,373 33,373 33,325 78,288"
              fill="none" stroke="var(--frame-line)" stroke-width="2"/>
  </svg>
  <div class="title-panel"></div>
  <h1 class="slide__title">Add<br>Your<br>Title<br>Here.</h1>
  <p class="slide__lede">We plan bold events with care and craft, from the first idea to the final bow. Every detail is shaped to help your brand stand out and be remembered.</p>
</section>

<section class="slide slide--nightshow">
  <svg class="slide__art" viewBox="0 0 705 396" preserveAspectRatio="none">
    <defs>
      <clipPath id="nightShape">
        <polygon points="0,0 355,0 705,273 705,396 128,396 0,268"/>
      </clipPath>
      <radialGradient id="nightRed" cx="0.5" cy="0.5" r="0.5">
        <stop offset="0" stop-color="#f0141c" stop-opacity="0.95"/>
        <stop offset="0.55" stop-color="#8a0a10" stop-opacity="0.6"/>
        <stop offset="1" stop-color="#8a0a10" stop-opacity="0"/>
      </radialGradient>
      <radialGradient id="nightTeal" cx="0.5" cy="0.5" r="0.5">
        <stop offset="0" stop-color="#3fa9a0" stop-opacity="0.55"/>
        <stop offset="1" stop-color="#3fa9a0" stop-opacity="0"/>
      </radialGradient>
      <radialGradient id="nightSmoke" cx="0.5" cy="0.5" r="0.5">
        <stop offset="0" stop-color="#bcbcc4" stop-opacity="0.45"/>
        <stop offset="1" stop-color="#bcbcc4" stop-opacity="0"/>
      </radialGradient>
      <radialGradient id="nightPink" cx="0.5" cy="0.5" r="0.5">
        <stop offset="0" stop-color="#d9709a" stop-opacity="0.45"/>
        <stop offset="1" stop-color="#d9709a" stop-opacity="0"/>
      </radialGradient>
    </defs>
    <g role="img" aria-label="Photo of fireworks bursting over a red-lit concert stage at night" clip-path="url(#nightShape)">
      <rect width="705" height="396" fill="#060606"/>
      <ellipse cx="250" cy="20" rx="140" ry="45" fill="url(#nightPink)"/>
      <ellipse cx="360" cy="150" rx="110" ry="90" fill="url(#nightTeal)"/>
      <ellipse cx="450" cy="220" rx="90" ry="55" fill="url(#nightSmoke)"/>
      <ellipse cx="430" cy="360" rx="300" ry="130" fill="url(#nightRed)"/>
      <ellipse cx="640" cy="330" rx="80" ry="110" fill="url(#nightRed)"/>
    </g>
    <polyline points="463,133 355,28 30,28 30,255 150,373 672,373 672,330 625,285"
              fill="none" stroke="var(--frame-line)" stroke-width="2"/>
  </svg>
  <h2 class="slide__title">Add<br>Your<br>Title<br>Here.</h2>
  <p class="slide__lede">We plan bold events with care and craft, from the first idea to the final bow. Every detail is shaped to help your brand stand out and be remembered.</p>
  <div class="info-panel">
    <p>Our team brings stage, light and sound together into one clear story. We work closely with each client so every show feels personal, sharp and true to its purpose.</p>
    <p>From launches to gala nights, we handle venues, crews and schedules with calm focus. Guests see a seamless evening while we keep every moving part in step behind the scenes.</p>
    <p>Results matter most. We measure reach, mood and feedback after each event, then share what worked and what comes next for your audience.</p>
  </div>
</section>

</body>
</html>
```